"leading industry company in search of a new web page"

we are searching for a clean, industry driven, engineered oriented web page design,

it need to be clean, and it need to have the chiefs company photo on the first page.
we are a mexican engineered company, we have 3 special sector specialties so in the front page we need to have a link to each one of these, and another one for CV "jobs" IM PUTING A COUPLE OD DESIGN IDEAL WITH OUR INFO SO YOU CAN PUT IT ALL TOGETHER

IM PUTING OUR LOGO AVAILABLE SO YOU CAN PUT IT IN THE PAGE

OUR WEB PAGE IS http://torvalen.com.mx

Target Market(s)

INDUSTRY LIKES ENERGY AND PETROL
COMPANIES IN THE ENGINEERING BUSINESS

Industry/Entity Type

Industry

Requirements
Must have
• CLEAN DESIGN,
• HIRING AND CV DEDICATED MENU TAB
• THE 3 DIVISIONS OF THE COMPANY
• SOCIAL MEDIA ON THE BOTTOM "JUST FACEBOOK AND TWITTER"
Nice to have
• COHERENCE WITH THE LOGO COLORS

```html
<!DOCTYPE html>
<html lang="es">
<head>
<meta charset="utf-8">
<title>Torvalen</title>
<link href="https://fonts.googleapis.com/css2?family=Source+Sans+3:wght@400;600;700&display=swap" rel="stylesheet">
<style>
:root{
  --red:#b3202c;
  --green:#5a9a12;
  --green-dark:#3f7a08;
  --text:#555;
  --nav-text:#555;
  --nav-active:#4a4b50;
  --footer:#5b5b5d;
  --line:#dcdcdc;
  --social:#2f6fb8;
}
*{box-sizing:border-box;margin:0;padding:0}
html,body{width:1092px;height:1200px;overflow:hidden;background:#fff}
body{position:relative;font-family:"Source Sans 3",Arial,sans-serif;color:var(--text)}
.abs{position:absolute}

.hero{left:0;top:0;width:1092px;height:480px;
  background:linear-gradient(180deg,#6b4a22 0%,#d9891b 22%,#f2b330 38%,#e58a1a 55%,#b0540f 72%,#5b2a0c 100%)}
.hero-arrow{width:48px;height:48px;border:2px solid rgba(255,255,255,.35);border-radius:50%}
.hero-arrow svg{display:block;margin:12px auto}
.hero-text{left:175px;bottom:94px;width:370px;color:#fff;font-size:10.5px;line-height:15.5px;letter-spacing:-0.1px;text-shadow:0 1px 2px rgba(0,0,0,.5)}
.btn-contact{left:178px;top:398px;width:129px;height:35px;background:linear-gradient(#e4e4e4,#a9a9a9);
  border-radius:3px;box-shadow:0 2px 3px rgba(0,0,0,.4);color:#555;font-size:13.5px;font-weight:600;
  text-align:center;line-height:35px}

.header{left:164px;top:0;width:764px;height:74px;background:#fff}
.brand{left:18px;top:0;height:74px;display:flex;align-items:center;gap:8px;font-size:26px;font-weight:700;color:var(--red)}
.brand-dot{width:22px;height:22px;border-radius:50%;background:var(--green)}
.nav a{position:absolute;top:0;height:74px;line-height:76px;font-size:10px;color:var(--nav-text);text-decoration:none;text-transform:uppercase}
.nav a.active{background:var(--nav-active);color:#fff;width:76px;text-align:center}

.division{top:504px;width:254px;text-align:center}
.division .photo{height:112px}
.division h2{margin-top:14px;font-size:13.5px;font-weight:400;color:var(--red);text-transform:uppercase}
.division p{margin:7px auto 0;width:220px;font-size:8.6px;line-height:14px}
.btn{display:block;background:linear-gradient(var(--green),var(--green-dark));color:#fff;font-size:8.5px;
  text-align:center;text-transform:uppercase;border-radius:2px;width:97px;height:26px;line-height:26px}
.division .btn{margin:12px auto 0}

.section-title{font-size:15.5px;font-weight:400;color:var(--red);text-transform:uppercase}
.about-photo{left:164px;top:814px;width:154px;height:133px;border:1px solid #ddd;padding:3px;background:#fff}
.about-photo div{width:100%;height:100%;background:linear-gradient(135deg,#e8e3db,#cbb9a4 55%,#f2efe9)}
.about-text{left:336px;top:813px;width:318px;font-size:8.6px;line-height:14px}

.news-item{left:686px;width:242px;height:84px;border-bottom:1px solid var(--line)}
.news-thumb{position:absolute;left:2px;top:0;width:64px;height:56px;border:1px solid #ddd;padding:2px;background:#fff}
.news-thumb div{width:100%;height:100%}
.news-body{position:absolute;left:83px;top:0;width:160px}
.news-body h3{font-size:8.2px;font-weight:600;color:var(--red);text-transform:uppercase;line-height:12px}
.news-body p{font-size:8.6px;line-height:14px;margin-top:2px}

.partner{top:1018px;width:149px;height:84px;border:1px solid #d4d4d4;display:flex;align-items:center;justify-content:center}

.footer{left:0;top:1133px;width:1092px;height:67px;background:var(--footer);color:#fff}
.footer-nav{left:168px;top:20px;font-size:7.5px;font-weight:600;text-transform:uppercase;display:flex;gap:0}
.footer-nav span{padding:0 17px}
.footer-nav span:first-child{padding-left:0}
.footer-nav i{font-style:normal}
.copyright{left:168px;top:38px;font-size:7.5px;font-weight:600;text-transform:uppercase}
.stay{left:774px;top:29px;font-size:7.5px;font-weight:600;text-transform:uppercase}
.social{top:21px;width:24px;height:24px;border-radius:50%;background:var(--social)}
</style>
</head>
<body>

<section class="hero abs" role="img" aria-label="Plataformas petroleras en el mar al atardecer">
  <div class="hero-arrow abs" style="left:77px;top:234px"><svg width="20" height="20" viewBox="0 0 20 20"><path d="M14 3 5 10l9 7z" fill="rgba(255,255,255,.35)"/></svg></div>
  <div class="hero-arrow abs" style="left:966px;top:234px"><svg width="20" height="20" viewBox="0 0 20 20"><path d="M6 3l9 7-9 7z" fill="rgba(255,255,255,.35)"/></svg></div>
  <p class="hero-text abs">Torvalen está constituida por un grupo de profesionales de amplia experiencia en el campo de la consultoría técnica y de gestión, con el principal objetivo de prestar servicios que ayuden a las empresas a mejorar la calidad y seguridad de sus productos e instalaciones así como su competitividad.</p>
  <a class="btn-contact abs">CONTACT US</a>
</section>

<header class="header abs">
  <div class="brand abs"><span class="brand-dot"></span>torvalen</div>
  <nav class="nav">
    <a class="active" style="left:232px">Home</a>
    <a style="left:327px">News</a>
    <a style="left:396px">About us</a>
    <a style="left:483px">Solutions</a>
    <a style="left:575px">Technologies</a>
    <a style="left:687px">Jobs / CV</a>
  </nav>
</header>

<article class="division abs" style="left:164px">
  <div class="photo" role="img" aria-label="Plataforma marina bajo cielo azul" style="background:linear-gradient(180deg,#3f78b8,#a9c6e2 55%,#2c5b8c)"></div>
  <h2>Industrial division</h2>
  <p>El área de competencia de este departamento se refiere a la totalidad de las actividades realizadas por Torvalen durante la aplicación de pruebas no destructivas en el campo industrial en cualquiera de...</p>
  <a class="btn">Read more</a>
</article>
<article class="division abs" style="left:419px">
  <div class="photo" role="img" aria-label="Bomba de extracción y trabajadores al atardecer" style="background:linear-gradient(180deg,#6a5a46,#c38a3a 60%,#2a1a0c)"></div>
  <h2>Verification division</h2>
  <p>El área de competencia de este departamento se refiere a la totalidad de las actividades realizadas por Torvalen durante la aplicación de pruebas no destructivas en el campo industrial en cualquiera de...</p>
  <a class="btn">Read more</a>
</article>
<article class="division abs" style="left:674px">
  <div class="photo" role="img" aria-label="Ingenieros frente a tanques de almacenamiento" style="background:linear-gradient(180deg,#2f6db3,#8fb3d8 50%,#3b4a78)"></div>
  <h2>Administration division</h2>
  <p>El área de competencia de este departamento se refiere a la totalidad de las actividades realizadas por Torvalen durante la aplicación de pruebas no destructivas en el campo industrial en cualquiera de...</p>
  <a class="btn">Read more</a>
</article>

<h2 class="section-title abs" style="left:163px;top:780px">About Torvalen</h2>
<div class="about-photo abs"><div role="img" aria-label="Retrato del director de la empresa"></div></div>
<p class="about-text abs">Torvalen está constituida por un grupo de profesionales de amplia experiencia en el campo de la consultoría técnica y de gestión, con el principal objetivo de prestar servicios que ayuden a las empresas a mejorar la calidad y seguridad de sus productos e instalaciones así como su competitividad.Más de 210 profesionales calificados y certificados se esfuerzan en participar con las pequeñas, medianas y grandes empresas, con su prestigio y credibilidad avalados por la experiencia en los grandes proyectos desarrollados en México, durante los últimos 32 años.</p>
<a class="btn abs" style="left:554px;top:926px">Read more</a>

<h2 class="section-title abs" style="left:685px;top:780px">Latest news</h2>
<div class="news-item abs" style="top:811px">
  <div class="news-thumb"><div role="img" aria-label="Plataforma marina" style="background:linear-gradient(#7b8fc0,#3a4e7a)"></div></div>
  <div class="news-body"><h3>Torvalen está constituida por un.</h3><p>Torvalen está constituida por un grupo de profesionales de amplia experiencia en el campo de la consultoría...</p></div>
</div>
<div class="news-item abs" style="top:895px">
  <div class="news-thumb"><div role="img" aria-label="Bomba de extracción al atardecer" style="background:linear-gradient(#7a6448,#c48a3a 60%,#2a1a0c)"></div></div>
  <div class="news-body"><h3>Torvalen está constituida por un.</h3><p>Torvalen está constituida por un grupo de profesionales de amplia experiencia en el campo de la consultoría...</p></div>
</div>
<div class="news-item abs" style="top:979px">
  <div class="news-thumb"><div role="img" aria-label="Trabajador con casco en planta" style="background:linear-gradient(#c9d2dc,#6d7884)"></div></div>
  <div class="news-body"><h3>Torvalen está constituida por un.</h3><p>Torvalen está constituida por un grupo de profesionales de amplia experiencia en el campo de la consultoría...</p></div>
</div>
<a class="btn abs" style="left:831px;top:1065px">View more</a>

<h2 class="section-title abs" style="left:163px;top:983px">Our partners</h2>
<div class="partner abs" style="left:164px" aria-label="Socio"><svg width="60" height="40"><rect x="10" y="4" width="40" height="32" rx="3" fill="#1c8a4a"/></svg></div>
<div class="partner abs" style="left:331px" aria-label="Socio"><svg width="60" height="40"><rect x="10" y="4" width="40" height="32" rx="3" fill="#1f7d3a"/></svg></div>
<div class="partner abs" style="left:498px" aria-label="Socio"><svg width="60" height="50"><circle cx="30" cy="25" r="22" fill="#c8222a"/></svg></div>

<footer class="footer abs">
  <div class="footer-nav abs">
    <span>Home</span><i>|</i><span>News</span><i>|</i><span>About us</span><i>|</i><span>Solutions</span><i>|</i><span>Technologies</span><i>|</i><span>Jobs/CV</span>
  </div>
  <div class="copyright abs">Copyrights 2013. Torvalen. All rights reserved.</div>
  <div class="stay abs">Stay connected :</div>
  <a class="social abs" style="left:845px" aria-label="Red social"></a>
  <a class="social abs" style="left:874px" aria-label="Red social"></a>
  <a class="social abs" style="left:902px" aria-label="Red social"></a>
</footer>

</body>
</html>
```